New Organic Skin Care Line Needs to Design a Product Label

***THE WINNER OF THIS PROJECT WILL MOST LIKELY BECOME THE EXCLUSIVE DESIGNER FOR OUR OTHER PRODUCT LABELS***

We need a label design for a new organic skin care product line called "Maple Fern Gala." This specific product is a 100% pure organic coconut oil. It's used for skin hydration, protection, and makeup removal.

Info to include on front label:

1. Logo: Maple Fern Gala (attached)
2. Product Name: Pure Coconut Oil (emphasize "organic" somewhere)
3. Slogan: Hydrate your skin and hair.
4. Size: 8 FL OZ 236mL

Attached is:

1. The brand logo "Maple Fern Gala" with a white background.
2. An image of the bottle we will use.
3. An image of the bottle with lines to show the size and placement of the label.
4. The brand logo "Maple Fern Gala" with a black background. (photoshop file)

What we need:

A simple mock up of the front side of the label on the bottle. We first want to know what it will look like on the bottle given the size and dimensions.

- We would like one label with a white background (including the logo with a white background).
- We would like a second label with a black background (including the logo with a black background, just need to make the black font white instead of black).

We can get a great idea of what to expect from the front side of the label so we will complete the back side once we identify a winner.
Updates

Apologies, but we are now using a different bottle. The previous one is now discontinued. Please view the two most recent images uploaded. One is an image of the new bottle by itself. The other is an image of that bottle with instructions. Please use your most recent designs on the new bottle. Feel free to make any modifications you see fit to compliment the new bottle shape. Added Friday, March 18, 2016

Reason: We are still working with the label company to finalize the size. Once the size is confirmed we will have to tweak labels based on finalized measurements.

Target Market(s)

Women, 18-70

Industry/Entity Type

Skin Care Product

Font styles to use
Decorative
Script

Requirements
Must have
• -"shabby sheek" and "cute" theme
• -soft organic feel
• -the ingredients are organic, pure, and natural. That should be an essence of the label.

```html
<!DOCTYPE html>
<html lang="en">
<head>
<meta charset="utf-8">
<title>Maple Fern Gala – Pure Coconut Oil Label</title>
<link rel="stylesheet" href="https://fonts.googleapis.com/css2?family=Cinzel:wght@400;700&family=Marcellus&display=swap">
<style>
  :root {
    --backdrop: #fbf1dc;
    --label-cream: #fbf8ee;
    --brand-ink: #3a2e2a;
    --pink-deep: #c8004f;
    --pink-bright: #f0206f;
    --gold-light: #fff2a6;
    --gold-mid: #e9c23a;
    --gold-deep: #b88a10;
    --title-ink: #fff6ea;
    --slogan-ink: #3b1a10;
    --coconut-brown: #9a5a2c;
    --coconut-flesh: #f4f0dc;
    --leaf-green: #3f9a3a;
  }
  html, body {
    margin: 0;
    padding: 0;
    width: 1200px;
    height: 1200px;
    overflow: hidden;
    background: var(--backdrop);
  }
  .canvas {
    width: 1200px;
    height: 1200px;
    display: block;
  }
  .brand-name {
    font-family: "Marcellus", serif;
    font-size: 46px;
    letter-spacing: 10px;
    fill: var(--brand-ink);
  }
  .product-title {
    font-family: "Cinzel", serif;
    font-weight: 700;
    font-size: 58px;
    letter-spacing: 2px;
    fill: var(--title-ink);
  }
  .product-title .cap { font-size: 72px; }
  .slogan {
    font-family: "Cinzel", serif;
    font-weight: 700;
    font-size: 25px;
    letter-spacing: 1px;
    fill: var(--slogan-ink);
  }
  .net-size {
    font-family: "Marcellus", serif;
    font-size: 20px;
    letter-spacing: 1.5px;
    fill: var(--title-ink);
  }
</style>
</head>
<body>
<svg class="canvas" viewBox="0 0 1200 1200" xmlns="http://www.w3.org/2000/svg">
  <defs>
    <clipPath id="label-clip">
      <circle cx="600" cy="600" r="500"/>
    </clipPath>
    <radialGradient id="pink-field" cx="50%" cy="70%" r="70%">
      <stop offset="0%" stop-color="var(--pink-bright)"/>
      <stop offset="100%" stop-color="var(--pink-deep)"/>
    </radialGradient>
    <linearGradient id="oil-wave" x1="0" y1="0" x2="1" y2="0">
      <stop offset="0%" stop-color="var(--gold-mid)"/>
      <stop offset="45%" stop-color="var(--gold-light)"/>
      <stop offset="70%" stop-color="var(--gold-deep)"/>
      <stop offset="100%" stop-color="var(--gold-mid)"/>
    </linearGradient>
    <linearGradient id="slogan-bar" x1="0" y1="0" x2="1" y2="0">
      <stop offset="0%" stop-color="var(--gold-mid)"/>
      <stop offset="50%" stop-color="var(--gold-light)"/>
      <stop offset="100%" stop-color="var(--gold-mid)"/>
    </linearGradient>
    <radialGradient id="coconut-fill" cx="50%" cy="45%" r="55%">
      <stop offset="0%" stop-color="var(--coconut-flesh)"/>
      <stop offset="55%" stop-color="var(--coconut-brown)"/>
      <stop offset="100%" stop-color="var(--leaf-green)" stop-opacity="0.6"/>
    </radialGradient>
  </defs>

  <g class="label" clip-path="url(#label-clip)">
    <rect class="label-top" x="100" y="100" width="1000" height="1000" fill="var(--label-cream)"/>
    <path class="label-field" fill="url(#pink-field)"
      d="M100 470 C 300 440, 420 520, 600 512 C 780 504, 900 420, 1100 390 L 1100 1100 L 100 1100 Z"/>
    <path class="oil-wave" role="img" aria-label="Golden coconut oil wave splash" fill="url(#oil-wave)"
      d="M100 450 C 300 420, 420 500, 600 490 C 780 480, 900 400, 1100 370
         L 1100 392 C 900 422, 780 506, 600 514 C 420 522, 300 444, 100 474 Z"/>
  </g>

  <text class="brand-name" x="600" y="350" text-anchor="middle">MAPLE FERN GALA</text>

  <text class="product-title" x="600" y="655" text-anchor="middle"><tspan class="cap">P</tspan>URE <tspan class="cap">C</tspan>OCONUT <tspan class="cap">O</tspan>IL</text>

  <rect class="slogan-band" x="310" y="672" width="580" height="38" fill="url(#slogan-bar)"/>
  <text class="slogan" x="600" y="700" text-anchor="middle">HYDRATE YOUR SKIN AND HAIR</text>

  <ellipse class="coconut-art" role="img" aria-label="Halved coconuts on green leaves with a 100% organic seal"
    cx="590" cy="870" rx="215" ry="120" fill="url(#coconut-fill)"/>

  <line x1="528" y1="1008" x2="672" y2="1008" stroke="var(--title-ink)" stroke-width="1" opacity="0.7"/>
  <text class="net-size" x="600" y="1032" text-anchor="middle">8 FL OZ 236mL</text>
  <line x1="528" y1="1042" x2="672" y2="1042" stroke="var(--title-ink)" stroke-width="1" opacity="0.7"/>
</svg>
</body>
</html>
```